Event Space Website (clone)

the name of the company is TOLVAPARTY.com
i’ll have a logo shortly

i basically need a clone of the following website
https://trovehallsnx.com/
i would really like the design to be with stock photos
and then after choosing the winner i will supply my photos
(im doing some all new photo shoots this week)

id love the designer to put their OWN spin on this site

Target Market(s)

nyc urban market

Industry/Entity Type

Event Planning

Coding

Coded - Design and coding required

Number of Pages Required

1 page

Font styles to use
Serif

Requirements
Must have
• from top to bottom ill just list what i need copied

LOCATIONS FAQ CONTACT AND SOCIAL MEDIA LINKS NEED

i need the slider ... for sure

please change classics to current locations
please show
Harlem
Brooklyn
Bronx (for bronx show an image of coming soon)

please change events with a view to
Harlem Venues
1. Tolva Northgate
2. Tolva East Northgate

please change Our biggest and boldest to Brooklyn Venues
1. Tolva Riverbend
2. Tolva Kingsfield (1)
3. Tolva kingsfield (2)
4. Tolva Kingsfield rooftop

remove latest ventures
remove asian couple kissing

keep interested in this location
keep why chose us

keep contact us area
keep social media plug in
Nice to have
• ur own flair and style

PLEASE dont forget that all the individual sections
example
tolva northgate
tolva east northgate
will have their own individual micro pages .... that will be placed under brooklyn venues (ive attached an example for clarity)

```html
<!DOCTYPE html>
<html lang="en">
<head>
<meta charset="utf-8">
<title>Tolva Party — Make Your Venue</title>
<link href="https://fonts.googleapis.com/css2?family=Noto+Serif:wght@400;700&family=Poppins:wght@400&display=swap" rel="stylesheet">
<style>
:root{
  --ink:#1b1b1b;
  --text:#333;
  --muted:#777;
  --white:#fff;
  --dark:#2b2b2b;
  --grey-band:#f3f3f3;
  --line:#cfcfcf;
  --black:#000;
  --brick:#9a5a44;
  --wood:#7a4a2c;
  --steel:#8e9296;
}
*{margin:0;padding:0;box-sizing:border-box}
html,body{width:1200px;height:3958px;overflow:hidden}
body{position:relative;background:var(--white);font-family:"Noto Serif",Georgia,serif;color:var(--text)}
.abs{position:absolute}
.site-header{left:0;top:0;width:1200px;height:63px;background:var(--white)}
.brand{left:129px;top:6px;width:81px;height:77px;background:var(--black);border:3px solid var(--white);outline:1px solid #ddd;display:flex;align-items:center;justify-content:center;color:var(--white);font-size:11px;font-weight:700;text-align:center;line-height:1.3;letter-spacing:.5px;z-index:3}
.main-nav{left:546px;top:23px;display:flex;font-size:13px;color:var(--ink)}
.main-nav span{margin-right:30px}
.main-nav span:last-child{margin-right:0}
.social{display:flex;gap:8px}
.social span{width:30px;height:30px;border:1px solid #ccc;display:flex;align-items:center;justify-content:center}
.social span i{width:8px;height:8px;border-radius:50%;background:var(--ink);display:block}
.header-social{left:998px;top:17px}

.hero{left:0;top:63px;width:1200px;height:505px;
  background:
    linear-gradient(180deg,rgba(0,0,0,0) 45%,rgba(8,8,14,.85) 78%,#07070c 100%),
    radial-gradient(ellipse 260px 200px at 860px 110px,rgba(255,90,120,.85),rgba(255,90,120,0)),
    radial-gradient(ellipse 320px 220px at 640px 80px,rgba(230,60,90,.7),rgba(230,60,90,0)),
    radial-gradient(ellipse 360px 260px at 220px 120px,rgba(70,110,230,.75),rgba(70,110,230,0)),
    radial-gradient(ellipse 300px 240px at 1080px 200px,rgba(90,90,200,.6),rgba(90,90,200,0)),
    radial-gradient(ellipse 420px 260px at 500px 260px,rgba(120,50,140,.55),rgba(120,50,140,0)),
    linear-gradient(180deg,#2a2248,#161428)}
.hero-title{left:0;top:290px;width:1200px;text-align:center;color:var(--white);font-size:39px;font-weight:700;letter-spacing:2px}
.dots{left:558px;top:539px;display:flex;gap:10px}
.dots i{width:7px;height:7px;border-radius:50%;background:rgba(255,255,255,.35)}
.dots i.on{background:rgba(255,255,255,.85)}

.sec-title{left:0;width:1200px;text-align:center;font-size:21px;font-weight:700;color:var(--ink)}
.sec-title::after{content:"";display:block;width:50px;height:2px;background:var(--ink);margin:8px auto 0}
.sec-title.light{color:var(--white)}
.sec-title.light::after{background:var(--white)}
.photo{position:absolute}
.caption{position:absolute;text-align:center;font-size:13px;color:var(--ink)}
.caption.light{color:var(--white)}

/* room tones: ceiling, wall, floor with window light */
.brick-room{background:
  radial-gradient(ellipse 60px 120px at 88% 42%,rgba(255,240,215,.75),rgba(255,240,215,0)),
  radial-gradient(ellipse 70% 22% at 50% 80%,rgba(230,170,110,.55),rgba(230,170,110,0)),
  linear-gradient(180deg,#3a2418 0%,#5e3a26 14%,#a4604a 18%,#b06c52 45%,#9a5a44 66%,#7a4a2c 70%,#a0683c 84%,#5a341e 100%)}
.loft-columns{background:
  radial-gradient(ellipse 45% 30% at 50% 46%,rgba(245,245,235,.85),rgba(245,245,235,0)),
  linear-gradient(90deg,rgba(0,0,0,0) 47%,rgba(110,70,40,.8) 48%,rgba(110,70,40,.8) 52%,rgba(0,0,0,0) 53%),
  linear-gradient(180deg,#1e1e20 0%,#3e3e40 16%,#c8ccc4 34%,#dcdcd2 52%,#b08a60 60%,#c49466 78%,#8a5a36 100%)}
.dark-hall{background:
  radial-gradient(ellipse 30% 25% at 30% 48%,rgba(140,150,120,.45),rgba(140,150,120,0)),
  linear-gradient(180deg,#1c1c1a 0%,#3a3a34 30%,#4e4e46 55%,#3a3a36 70%,#2a2a28 100%)}
.marble-hall{background:
  radial-gradient(ellipse 30% 50% at 86% 40%,rgba(200,225,240,.9),rgba(200,225,240,0)),
  radial-gradient(ellipse 40% 25% at 60% 82%,rgba(255,255,255,.9),rgba(255,255,255,0)),
  linear-gradient(180deg,#f2f2f0 0%,#e4e2dc 35%,#6a6662 50%,#cfcfcc 60%,#e8e8e6 80%,#a8a8a6 100%)}
.white-hall{background:
  radial-gradient(ellipse 40% 30% at 80% 42%,rgba(190,215,235,.9),rgba(190,215,235,0)),
  linear-gradient(90deg,rgba(0,0,0,0) 46%,rgba(235,238,240,.9) 47%,rgba(235,238,240,.9) 52%,rgba(0,0,0,0) 53%),
  linear-gradient(180deg,#f4f5f6 0%,#e2e5e8 40%,#c4c8cb 56%,#b4b8ba 75%,#9aa0a3 100%)}
.warehouse-brick{background:
  radial-gradient(ellipse 40% 18% at 50% 8%,rgba(230,220,200,.7),rgba(230,220,200,0)),
  radial-gradient(ellipse 50% 22% at 50% 80%,rgba(220,215,205,.8),rgba(220,215,205,0)),
  linear-gradient(180deg,#5a4e46 0%,#7a6a5e 16%,#8e5a48 28%,#9a6250 50%,#b8b0a6 62%,#cac4bc 82%,#a8a29a 100%)}
.steel-hall{background:
  radial-gradient(ellipse 40% 25% at 50% 10%,rgba(245,248,250,.9),rgba(245,248,250,0)),
  linear-gradient(180deg,#d4d8dc 0%,#9ea4a8 22%,#c8ccce 42%,#80827e 62%,#a2a29c 78%,#6c6c68 100%)}

.dark-band{left:0;top:1080px;width:1200px;height:508px;background:radial-gradient(ellipse at 50% 40%,#383838,#252525 75%)}
.grey-band{left:0;top:2411px;width:1200px;height:389px;background:var(--grey-band)}
.step{position:absolute;top:2545px;width:187px;height:183px;background:var(--white);border-right:4px solid var(--line);border-bottom:4px solid var(--line);text-align:center}
.step b.num{position:absolute;left:5px;top:10px;width:28px;height:28px;background:#3a3a3a;color:var(--white);font-size:11px;display:flex;align-items:center;justify-content:center}
.step svg{margin-top:46px}
.step h4{font-size:11px;font-weight:700;color:var(--ink);margin:6px 24px 4px;line-height:1.35}
.step p{font-size:11px;color:var(--muted);margin:0 20px;line-height:1.35}
.step p b{color:var(--ink)}

.why-band{left:0;top:2800px;width:1200px;height:369px;background:
  radial-gradient(ellipse 300px 160px at 180px 260px,rgba(90,70,80,.55),rgba(90,70,80,0)),
  radial-gradient(ellipse 300px 160px at 1000px 120px,rgba(70,80,110,.55),rgba(70,80,110,0)),
  radial-gradient(ellipse 400px 180px at 600px 300px,rgba(60,50,60,.5),rgba(60,50,60,0)),
  linear-gradient(180deg,#1e2433,#262a35 50%,#1c1f29)}
.why-card{position:absolute;top:2949px;width:171px;height:149px;background:var(--white);text-align:center;font-size:14px;color:var(--ink)}
.why-card svg{margin-top:30px}
.why-card .label{position:absolute;left:0;right:0;bottom:18px}
.why-card.tall{top:2928px;height:192px}
.why-card.tall p{font-size:11px;margin:12px 18px 0;line-height:1.45}

.field-label{position:absolute;font-size:11px;font-weight:700;color:var(--ink)}
.input{position:absolute;border:1px solid #ddd;background:var(--white)}
.checks{position:absolute;left:227px;display:flex;font-family:"Poppins",sans-serif;font-size:9px;color:#888}
.checks span{display:flex;align-items:center;margin-right:20px}
.checks span::before{content:"";width:13px;height:13px;border:1px solid #bbb;margin-right:6px}
.submit{left:542px;top:3608px;width:115px;height:32px;background:var(--black);color:var(--white);font-size:13px;display:flex;align-items:center;justify-content:center}

.gallery{left:0;top:3712px;width:1200px;height:171px;display:flex}
.gallery div{flex:1}
.gallery-mark{left:759px;top:3785px;width:22px;height:22px;border:2px solid var(--white);border-radius:50%}
.site-footer{left:0;top:3883px;width:1200px;height:75px;background:var(--black)}
.footer-nav{left:129px;top:3897px;display:flex;font-size:11px;color:#ddd}
.footer-nav span{margin-right:30px}
.copyright{left:129px;top:3921px;font-size:11px;color:#bbb}
.footer-social{left:1002px;top:3896px}
.footer-social span{border-color:#444}
.footer-social span i{background:var(--white)}
</style>
</head>
<body>

<header class="site-header abs"></header>
<div class="brand abs">TOLVA<br>PARTY</div>
<nav class="main-nav abs"><span>Locations</span><span>Faq</span><span>E-Brochure</span><span>Preferred Vendors</span><span>Contact</span></nav>
<div class="social header-social abs"><span><i></i></span><span><i></i></span></div>

<section class="hero abs" role="img" aria-label="Concert crowd with raised hands under colourful stage lights"></section>
<h1 class="hero-title abs">MAKE YOUR VENUE</h1>
<div class="dots abs"><i></i><i></i><i></i><i class="on"></i><i></i></div>

<h2 class="sec-title abs" style="top:638px">Current Locations</h2>
<div class="photo brick-room" role="img" aria-label="Harlem brick-walled loft with wood floors and arched windows" style="left:129px;top:707px;width:300px;height:276px"></div>
<div class="photo loft-columns" role="img" aria-label="Brooklyn open loft with columns and bright windows" style="left:450px;top:707px;width:300px;height:276px"></div>
<div class="photo dark-hall" role="img" aria-label="Bronx venue coming soon, dim industrial hall" style="left:771px;top:707px;width:300px;height:276px"></div>
<p class="caption" style="left:129px;top:995px;width:300px">Harlem</p>
<p class="caption" style="left:450px;top:995px;width:300px">Brooklyn</p>
<p class="caption light" style="left:771px;top:955px;width:300px">Bronx</p>

<section class="dark-band abs"></section>
<h2 class="sec-title light abs" style="top:1146px">Events with a view to Harlem Venues</h2>
<div class="photo marble-hall" role="img" aria-label="Tolva Northgate bright hall with marble floor and river windows" style="left:129px;top:1216px;width:459px;height:277px"></div>
<div class="photo white-hall" role="img" aria-label="Tolva East Northgate open white hall with window wall" style="left:611px;top:1216px;width:460px;height:277px"></div>
<p class="caption light" style="left:129px;top:1505px;width:459px">Tolva Northgate</p>
<p class="caption light" style="left:611px;top:1505px;width:460px">Tolva East Northgate</p>

<h2 class="sec-title abs" style="top:1656px">Brooklyn Venues</h2>
<div class="photo loft-columns" role="img" aria-label="Tolva Riverbend loft with wood floor and columns" style="left:129px;top:1726px;width:459px;height:277px"></div>
<div class="photo warehouse-brick" role="img" aria-label="Tolva Kingsfield brick warehouse with high roof" style="left:611px;top:1726px;width:460px;height:277px"></div>
<div class="photo steel-hall" role="img" aria-label="Tolva Kingsfield industrial hall with skylight and balconies" style="left:129px;top:2064px;width:459px;height:277px"></div>
<div class="photo brick-room" role="img" aria-label="Tolva Kingsfield rooftop brick room with arched windows" style="left:611px;top:2064px;width:460px;height:277px"></div>
<p class="caption" style="left:129px;top:2015px;width:459px">Tolva Riverbend</p>
<p class="caption" style="left:611px;top:2015px;width:460px">Tolva Kingsfield</p>
<p class="caption" style="left:129px;top:2353px;width:459px">Tolva Kingsfield</p>
<p class="caption" style="left:611px;top:2353px;width:460px">Tolva Kingsfield rooftop</p>

<section class="grey-band abs"></section>
<h2 class="sec-title abs" style="top:2474px">Events with a view to Harlem Venues</h2>
<div class="step" style="left:174px"><b class="num">01</b>
  <svg width="40" height="36" viewBox="0 0 40 36" fill="none" stroke="#999" stroke-width="1.5"><rect x="12" y="4" width="20" height="26"/><path d="M16 12h12M16 17h12M16 22h8M6 14l8 8v10H6z"/></svg>
  <h4>SEND US A NOTE</h4><p>We don't keep you waiting</p></div>
<div class="step" style="left:384px"><b class="num">02</b>
  <svg width="40" height="36" viewBox="0 0 40 36" fill="none" stroke="#999" stroke-width="1.5"><path d="M20 33s-10-11-10-18a10 10 0 0 1 20 0c0 7-10 18-10 18z"/><circle cx="20" cy="15" r="4"/></svg>
  <h4>CHECK OUT THE LOCATION</h4><p>Take a guided tour with a venue rep</p></div>
<div class="step" style="left:593px"><b class="num">03</b>
  <svg width="40" height="36" viewBox="0 0 40 36" fill="none" stroke="#999" stroke-width="1.5"><rect x="6" y="6" width="28" height="26"/><path d="M6 13h28M13 2v7M27 2v7M12 19h2M19 19h2M26 19h2M12 25h2M19 25h2"/></svg>
  <h4>PICK YOUR PERFECT DATE</h4><p>We can help you find the right date</p></div>
<div class="step" style="left:802px"><b class="num">04</b>
  <svg width="40" height="36" viewBox="0 0 40 36" fill="none" stroke="#999" stroke-width="1.5"><path d="M8 8l4 4M12 8l-4 4M28 24l4 4M32 24l-4 4M10 30h4M10 16v10M16 10h8l4 6"/></svg>
  <h4>PLAN</h4><p>Check out our <b>Vendors</b> have <b>Questions?</b></p></div>

<section class="why-band abs" role="img" aria-label="Dim crowd at an evening event"></section>
<h2 class="sec-title light abs" style="top:2864px">Why choose us?</h2>
<div class="why-card" style="left:129px">
  <svg width="40" height="46" viewBox="0 0 40 46" fill="none" stroke="#222" stroke-width="1.8"><path d="M12 20V8a3 3 0 0 1 6 0v12M18 18v-4a3 3 0 0 1 6 0v6M24 18a3 3 0 0 1 6 0v8c0 9-5 14-12 14s-11-5-12-10l-2-8a3 3 0 0 1 6-1l2 5"/></svg>
  <span class="label">Easy</span></div>
<div class="why-card tall" style="left:321px">
  <svg width="44" height="40" viewBox="0 0 44 40" fill="none" stroke="#222" stroke-width="1.8"><path d="M4 4h28v20H16l-8 6v-6H4z"/><path d="M10 11h16M10 17h12M36 14h4v18h-4v5l-6-5H18v-4"/></svg>
  <p>Talk to us-we're there to help answer all your questions</p>
  <span class="label">Responsive</span></div>
<div class="why-card" style="left:513px">
  <svg width="44" height="44" viewBox="0 0 44 44" fill="none" stroke="#222" stroke-width="1.8"><circle cx="22" cy="22" r="7"/><path d="M22 4v6M22 34v6M4 22h6M34 22h6M9 9l4 4M31 31l4 4M35 9l-4 4M13 31l-4 4"/><circle cx="22" cy="22" r="13"/></svg>
  <span class="label">Customizable</span></div>
<div class="why-card" style="left:705px">
  <svg width="44" height="44" viewBox="0 0 44 44" fill="none" stroke="#222" stroke-width="1.8"><path d="M6 6h32v6H6zM8 12v26h28V12M16 38V26h12v12"/><circle cx="22" cy="19" r="3"/></svg>
  <span class="label">Vendors</span></div>
<div class="why-card" style="left:899px">
  <svg width="44" height="44" viewBox="0 0 44 44" fill="none" stroke="#222" stroke-width="1.8"><circle cx="22" cy="22" r="16"/><circle cx="22" cy="22" r="9"/><path d="M10 10l24 24"/></svg>
  <span class="label">Transparent</span></div>

<h2 class="sec-title abs" style="top:3235px">Send Us A Message</h2>
<span class="field-label" style="left:227px;top:3307px">Name</span>
<span class="field-label" style="left:482px;top:3307px">Email</span>
<span class="field-label" style="left:737px;top:3307px">Phone</span>
<div class="input" style="left:227px;top:3327px;width:234px;height:28px"></div>
<div class="input" style="left:482px;top:3327px;width:234px;height:28px"></div>
<div class="input" style="left:737px;top:3327px;width:235px;height:28px"></div>
<span class="field-label" style="left:227px;top:3374px">Venue(s) of interest</span>
<div class="checks" style="top:3404px"><span>Pier Nine</span><span>Harbor Point</span><span>Kingsfield cyc</span><span>Kingsfield expo hall</span><span>Dockside loft</span><span>Maplewood Loft</span></div>
<div class="checks" style="top:3434px"><span>Maplewood terminal depot</span><span>Metro expo hall</span><span>River princess</span><span>Highloft</span><span>Z Loft</span></div>
<span class="field-label" style="left:227px;top:3473px">Type of Event</span>
<span class="field-label" style="left:610px;top:3473px">Message</span>
<div class="input" style="left:227px;top:3491px;width:361px;height:80px"></div>
<div class="input" style="left:610px;top:3491px;width:362px;height:80px"></div>
<div class="submit abs">Submit</div>

<div class="gallery abs">
  <div role="img" aria-label="Host speaking at an event" style="background:radial-gradient(ellipse at 45% 45%,#3a3a3a,rgba(58,58,58,0) 40%),linear-gradient(180deg,#eeeeee,#b8b8b4 50%,#2a3020)"></div>
  <div role="img" aria-label="Couple at a wedding in a loft" style="background:radial-gradient(ellipse at 55% 60%,#e8e4de,rgba(232,228,222,0) 45%),linear-gradient(180deg,#4a3a30,#8a7a6a 50%,#c8c0b6)"></div>
  <div role="img" aria-label="Guest in a suit at a waterfront venue" style="background:radial-gradient(ellipse at 55% 55%,#6a4a8a,rgba(106,74,138,0) 40%),linear-gradient(180deg,#1e2a48,#3a4a6a 50%,#8a8aa0)"></div>
  <div role="img" aria-label="City skyline with picnic tables" style="background:linear-gradient(180deg,#5a8ad0 0%,#8ab0e0 30%,#5a6a80 45%,#c89a50 65%,#e0b060 85%,#d07aa0 100%)"></div>
  <div role="img" aria-label="Party in a dim venue with string lights" style="background:radial-gradient(ellipse at 50% 15%,#8a6a50,rgba(138,106,80,0) 50%),linear-gradient(180deg,#4a302a,#3a2420 60%,#5a4030)"></div>
  <div role="img" aria-label="Floral table setting" style="background:radial-gradient(ellipse at 30% 70%,#4a6a2a,rgba(74,106,42,0) 45%),linear-gradient(180deg,#6a4a2a,#c8a46a 50%,#8a6a3a)"></div>
  <div role="img" aria-label="Long dining tables in a hall" style="background:radial-gradient(ellipse at 50% 25%,#d8d8d4,rgba(216,216,212,0) 45%),linear-gradient(180deg,#8a8a86,#6a6258 55%,#3a3028)"></div>
</div>
<div class="gallery-mark abs"></div>

<footer class="site-footer abs"></footer>
<nav class="footer-nav abs"><span>Locations</span><span>Faq</span><span>E-Brochure</span><span>Preferred Vendors</span><span>Contact</span></nav>
<p class="copyright abs">Copyright © 2021 Tolva Party. All Rights Reserved</p>
<div class="social footer-social abs"><span><i></i></span><span><i></i></span></div>

</body>
</html>
```